Whiskey label design and bottle design

We need a label design for our new whiskey company. We are going to use paper logo that can include any elements that the designer wants including shinny, glossy, etc. We need something eye catching that stands out. Our bottle has not been chosen so we are can use any type of bottle including a custom bottle. Something that looks expensive. High quality. Need to stand out. The Brand name for now is the Heart of Marrowdale

Target Market(s)

21 to 54 60% male, 40% female

Industry/Entity Type

Whiskey Spirits

Requirements
Must have
• Detailed packaging, A barcode for the SKU, Governement warning on the back, Area for a story on the back, size of bottle on the back, Cork Closure.
Nice to have
• Something with tradition, Quality, and it stands out from comeptors. High quality labels.

```html
<!DOCTYPE html>
<html lang="en">
<head>
<meta charset="utf-8">
<title>Heart of Marrowdale – Special Reserve Whisky Label</title>
<link rel="stylesheet" href="https://fonts.googleapis.com/css2?family=Rye&family=Alfa+Slab+One&family=Pinyon+Script&family=Josefin+Slab:wght@700&family=Cinzel:wght@600;700&family=Oswald:wght@500&display=swap">
<style>
  :root {
    --backdrop: #0b0b0b;
    --paper: #e9e5dc;
    --paper-edge: #dcd6ca;
    --ink: #262626;
    --ink-soft: #3c3c3c;
    --gold: #b38c4e;
    --gold-light: #d7b57a;
    --burgundy: #9c3b47;
    --burgundy-faint: rgba(156, 59, 71, 0.55);
    --stripe: #8d8d8d;
  }
  * { box-sizing: border-box; margin: 0; padding: 0; }
  html, body { width: 1200px; height: 1200px; overflow: hidden; background: var(--backdrop); }
  .canvas { position: relative; width: 1200px; height: 1200px; background: var(--backdrop); }

  .label {
    position: absolute; left: 200px; top: 100px; width: 800px; height: 1000px;
    background: linear-gradient(90deg, var(--paper-edge) 0%, var(--paper) 8%, var(--paper) 92%, var(--paper-edge) 100%);
    color: var(--ink); overflow: hidden;
  }
  .rule { position: absolute; left: 16px; right: 16px; background: var(--ink); }
  .rule--top-thick { top: 12px; height: 5px; }
  .rule--top-thin { top: 24px; height: 2px; }
  .rule--gold { top: 940px; height: 4px; background: linear-gradient(90deg, var(--gold), var(--gold-light), var(--gold)); }
  .band--bottom { position: absolute; left: 16px; right: 16px; top: 954px; height: 34px; background: var(--ink); }

  .line { position: absolute; left: 0; right: 0; text-align: center; white-space: nowrap; }
  .special-reserve { top: 50px; font: 700 20px/1 "Cinzel", serif; letter-spacing: 5px; }
  .brand-main { top: 112px; font: 128px/1 "Rye", serif; letter-spacing: 2px; }
  .brand-of { top: 256px; font: 34px/1 "Rye", serif; }
  .brand-place { top: 300px; font: 60px/1 "Rye", serif; letter-spacing: 1px; }
  .tagline { top: 392px; font: 700 17px/1 "Cinzel", serif; letter-spacing: 2px; }
  .product { top: 440px; font: 106px/1 "Alfa Slab One", serif; letter-spacing: 6px; }
  .cask-line { top: 568px; }
  .cask-line .script { font: 32px/1 "Pinyon Script", cursive; color: var(--ink); margin-right: 14px; }
  .cask-line .cask { font: 600 34px/1 "Cinzel", serif; letter-spacing: 4px; color: var(--gold); }
  .quality { top: 636px; font: 700 30px/1 "Josefin Slab", serif; letter-spacing: 3px; }
  .style { top: 688px; font: 500 24px/1.35 "Oswald", sans-serif; letter-spacing: 3px; }
  .dots { position: absolute; left: 265px; right: 265px; top: 752px; border-top: 3px dotted var(--ink-soft); }
  .batch { top: 790px; display: flex; justify-content: center; align-items: center; gap: 22px; }
  .batch .word { font: 500 25px/1 "Oswald", sans-serif; letter-spacing: 3px; }
  .batch .script { font: 52px/1 "Pinyon Script", cursive; color: var(--gold); }
  .finish { top: 860px; font: 500 28px/1 "Oswald", sans-serif; letter-spacing: 3px; }
  .sourced { top: 904px; font: 700 17px/1 "Cinzel", serif; letter-spacing: 4px; }

  .ornament { position: absolute; }
  .ornament--left { left: 120px; top: 690px; width: 90px; height: 70px; }
  .ornament--right { right: 120px; top: 690px; width: 90px; height: 70px; }
  .ornament--low-left { left: 148px; top: 790px; width: 36px; height: 90px; }
  .ornament--low-right { right: 148px; top: 790px; width: 36px; height: 90px; }

  .side-panel { position: absolute; top: 475px; width: 34px; height: 420px; }
  .side-panel--left { left: 20px; }
  .side-panel--right { right: 22px; }

  .vertical { position: absolute; white-space: nowrap; transform-origin: center; }
  .volume { left: 34px; top: 708px; transform: rotate(-90deg); font: 500 16px/1 "Oswald", sans-serif; letter-spacing: 2px; }
  .strength { right: 20px; top: 708px; transform: rotate(90deg); font: 500 16px/1 "Oswald", sans-serif; letter-spacing: 2px; }
  .batch-note {
    left: -110px; top: 250px; width: 300px; transform: rotate(-90deg);
    font: 700 11px/1.35 "Cinzel", serif; letter-spacing: 2px; color: var(--burgundy); text-align: center;
  }

  .brand-seal { position: absolute; left: 655px; top: 80px; width: 260px; height: 280px; }
  .brand-seal .ring { position: absolute; left: 20px; top: 30px; width: 200px; height: 200px; border: 3px solid var(--burgundy-faint); border-radius: 50%; }
  .brand-seal .name { position: absolute; left: 40px; top: 110px; font: 700 18px/1.3 "Cinzel", serif; letter-spacing: 3px; color: var(--burgundy-faint); }
</style>
</head>
<body>
<main class="canvas">
  <section class="label" aria-label="Heart of Marrowdale front label">
    <div class="rule rule--top-thick"></div>
    <div class="rule rule--top-thin"></div>

    <div class="brand-seal">
      <div class="ring"></div>
      <div class="name">HEART OF<br>MARROWDALE</div>
    </div>

    <div class="vertical batch-note">EXTRAORDINARY SPIRIT<br>THIS BEING BATCH Nº 0834</div>

    <p class="line special-reserve">· SPECIAL RESERVE ·</p>
    <h1 class="line brand-main">HEART</h1>
    <p class="line brand-of">OF</p>
    <p class="line brand-place">MARROWDALE</p>
    <p class="line tagline">EXTRAORDINARY SPIRIT</p>
    <h2 class="line product">WHISKY</h2>
    <p class="line cask-line"><span class="script">Made With</span><span class="cask">CASK STRENGTH</span></p>
    <p class="line quality">SPIRIT OF THE FINEST QUALITY</p>
    <p class="line style">AMERICAN SINGLE<br>MALT WHISKY</p>
    <div class="dots"></div>
    <p class="line batch"><span class="word">SMALL</span><span class="script">Handcrafted</span><span class="word">BATCH</span></p>
    <p class="line finish">FINISHED IN BOURBON CASK</p>
    <p class="line sourced">LOCALLY SOURCED INGREDIENTS</p>

    <svg class="ornament ornament--left" role="img" aria-label="Scrolled flourish ornament" viewBox="0 0 90 70"><rect width="90" height="70" rx="30" fill="#3c3c3c" opacity="0.18"/></svg>
    <svg class="ornament ornament--right" role="img" aria-label="Scrolled flourish ornament" viewBox="0 0 90 70"><rect width="90" height="70" rx="30" fill="#3c3c3c" opacity="0.18"/></svg>
    <svg class="ornament ornament--low-left" role="img" aria-label="Small vine flourish" viewBox="0 0 36 90"><rect width="36" height="90" rx="16" fill="#3c3c3c" opacity="0.14"/></svg>
    <svg class="ornament ornament--low-right" role="img" aria-label="Small vine flourish" viewBox="0 0 36 90"><rect width="36" height="90" rx="16" fill="#3c3c3c" opacity="0.14"/></svg>

    <svg class="side-panel side-panel--left" role="img" aria-label="Engraved line pattern panel" viewBox="0 0 34 420" preserveAspectRatio="none"><rect width="34" height="420" fill="#8d8d8d" opacity="0.7"/></svg>
    <svg class="side-panel side-panel--right" role="img" aria-label="Engraved line pattern panel" viewBox="0 0 34 420" preserveAspectRatio="none"><rect width="34" height="420" fill="#8d8d8d" opacity="0.7"/></svg>

    <span class="vertical volume">750ML</span>
    <span class="vertical strength">45% ALC</span>

    <div class="rule rule--gold"></div>
    <div class="band--bottom"></div>
  </section>
</main>
</body>
</html>
```